Fore Sale sign for my real estate agency

I am a Brisbane - Australia inner western suburbs boutique real estate agent who is needing a for sale sign. We are a small dynamic family agency that needs a for sale sign that will standout and give us a strong presence in the market.

I have attached a logo I like, however I am not fixed on anything and am open to suggestions.

The information on the sign should contain but not necessarily limited to the following information - please appreciate I am very open
1 logo - O'Venny
2 Ph number - 3847 1952
3 web address - ovenny.com.au

Thank you
Gareth O'Venny

```html
<!DOCTYPE html>
<html lang="en">
<head>
<meta charset="utf-8">
<title>O'Venny – For Sale Sign</title>
<link rel="stylesheet" href="https://fonts.googleapis.com/css2?family=Days+One&family=Comfortaa:wght@700&display=swap">
<style>
  :root {
    --sign-orange: #ea9424;
    --sign-white: #ffffff;
  }
  html, body {
    margin: 0;
    padding: 0;
    width: 1200px;
    height: 800px;
    overflow: hidden;
    background: var(--sign-orange);
  }
  .sale-sign {
    display: block;
    width: 1200px;
    height: 800px;
  }
  .sign-board { fill: var(--sign-orange); }
  .headline {
    font-family: "Days One", "Arial Black", sans-serif;
    fill: var(--sign-white);
  }
  .agency-name {
    font-family: "Days One", "Arial Black", sans-serif;
    fill: var(--sign-white);
  }
  .contact-phone,
  .contact-web {
    font-family: "Comfortaa", "Varela Round", sans-serif;
    font-weight: 700;
    fill: var(--sign-white);
  }
</style>
</head>
<body>
  <svg class="sale-sign" viewBox="0 0 1200 800" xmlns="http://www.w3.org/2000/svg" role="img" aria-label="O'Venny for sale sign">
    <rect class="sign-board" x="0" y="0" width="1200" height="800"/>

    <text class="headline" x="62" y="234" font-size="282" textLength="1080" lengthAdjust="spacingAndGlyphs">FOR SALE</text>

    <text class="agency-name" x="600" y="502" font-size="150" text-anchor="middle" textLength="540" lengthAdjust="spacingAndGlyphs">O'Venny</text>

    <text class="contact-phone" x="183" y="646" font-size="124" textLength="847" lengthAdjust="spacingAndGlyphs">CALL: 3847-1952</text>

    <text class="contact-web" x="215" y="750" font-size="112" textLength="745" lengthAdjust="spacingAndGlyphs">ovenny.com.au</text>
  </svg>
</body>
</html>
```